Präsentationsvorlagen / Powerpoint Master for my company
Zielgruppe
Offline hardware device to manage and save passwords safely.
Aufgabenstellung
DIN A4 quer

```html
<!DOCTYPE html>
<html lang="en">
<head>
<meta charset="utf-8">
<title>Vaultline Presentation Master</title>
<link rel="stylesheet" href="https://fonts.googleapis.com/css2?family=Montserrat:wght@300;400;600;700;800&display=swap">
<style>
  :root {
    --green: #2e7a3c;
    --ink: #141518;
    --paper: #f3f3f3;
    --slide: #f8f8f9;
    --text-grey: #4a4c50;
    --shade: #e4e5e8;
  }
  * { box-sizing: border-box; margin: 0; padding: 0; }
  html, body { width: 882px; height: 1200px; overflow: hidden; }
  body {
    background: var(--paper);
    font-family: "Montserrat", Arial, sans-serif;
    color: var(--ink);
    position: relative;
  }

  .slide {
    position: absolute;
    overflow: hidden;
    background: var(--slide);
    box-shadow: 0 4px 14px rgba(0,0,0,.12);
  }
  .slide--small { width: 360px; height: 255px; font-size: 4.95px; }
  .slide--large { left: 77px; top: 628px; width: 728px; height: 515px; font-size: 10px; }

  .facets { position: absolute; inset: 0; width: 100%; height: 100%; }

  .slide__header {
    position: absolute; left: 5.5%; top: 14.5%;
    font-size: 2.2em; font-weight: 700; white-space: nowrap;
  }
  .slide__header em { font-style: normal; color: var(--green); }

  .brand-name {
    position: absolute; right: 4.5%; top: 11.5%;
    font-size: 3.2em; font-weight: 700; color: var(--ink); letter-spacing: .01em;
  }

  .slide__footer {
    position: absolute; left: 0; right: 0; bottom: 0; height: 5.2%;
    background: var(--ink);
  }
  .slide__footer-title {
    position: absolute; left: 4.6%; top: 50%; transform: translateY(-50%);
    color: #fff; font-size: 1.15em; font-weight: 700; white-space: nowrap;
  }
  .page-tab {
    position: absolute; right: 0; bottom: 0; width: 13.5%; height: 7%;
    background: var(--green); border-top-left-radius: 2.2em;
    color: #fff; font-weight: 700; font-size: 1.7em;
    display: flex; align-items: center; justify-content: center;
  }

  .photo { position: absolute; }

  .lead { position: absolute; line-height: 1.05; }
  .lead__light { display: block; font-size: 3em; font-weight: 300; color: var(--text-grey); }
  .lead__bold { display: block; font-size: 3.2em; font-weight: 700; color: var(--green); }

  .body-copy {
    position: absolute; font-size: 1.05em; line-height: 1.55; color: var(--text-grey);
  }

  .accent-triangle { position: absolute; width: 7%; height: 9%; }

  /* title slide */
  .slide--title { background: #1c1c1d; }
  .slide--title .photo { inset: 0; background: linear-gradient(160deg, #3a3b3d 0%, #232425 45%, #121213 100%); }
  .title-brand {
    position: absolute; left: 40%; top: 30%;
    font-size: 3.8em; font-weight: 700; color: #fff;
  }
  .title-block { position: absolute; left: 40%; top: 45%; color: #fff; line-height: 1.1; }
  .title-block__light { display: block; font-size: 3.2em; font-weight: 300; }
  .title-block__bold { display: block; font-size: 3.5em; font-weight: 800; }
  .title-copy {
    position: absolute; left: 40%; top: 70%; width: 48%;
    font-size: 1.05em; line-height: 1.55; color: #c9c9c9;
  }
  .slide--title .page-tab { height: 8%; width: 16%; }

  /* feature columns */
  .feature { position: absolute; top: 66%; width: 26%; }
  .feature__icon { width: 3.4em; height: 3.4em; display: block; margin-bottom: .6em; }
  .feature__title { font-size: 1.5em; font-weight: 700; color: var(--green); margin-bottom: .5em; }
  .feature__text { font-size: 1.05em; line-height: 1.55; color: var(--text-grey); }
</style>
</head>
<body>

<!-- Title slide -->
<section class="slide slide--small slide--title" style="left:66px; top:40px;">
  <div class="photo" role="img" aria-label="Dimmed office interior with people walking past large windows"></div>
  <div class="title-brand">Vaultline</div>
  <div class="title-block">
    <span class="title-block__light">Your Presentation</span>
    <span class="title-block__bold">Title Goes Here</span>
  </div>
  <p class="title-copy">Lorem ipsum dolor sit amet, consectetur adipiscing elit, sed do eiusmod tempor incididunt ut labore et dolore magna aliqua.</p>
  <div class="page-tab"></div>
</section>

<!-- Slide 01 -->
<section class="slide slide--small" style="left:456px; top:40px;">
  <svg class="facets" viewBox="0 0 728 515" preserveAspectRatio="none" aria-hidden="true">
    <rect width="728" height="515" fill="#f7f7f8"/>
    <polygon points="0,0 250,0 0,170" fill="#ffffff"/>
    <polygon points="380,0 728,0 728,90 430,300 130,300" fill="#eeeef0"/>
    <polygon points="728,180 728,515 300,515" fill="#ffffff"/>
  </svg>
  <h2 class="slide__header"><em>Header</em> Goes Here</h2>
  <div class="brand-name">Vaultline</div>
  <div class="lead" style="left:10%; top:34%;">
    <span class="lead__light">Lorem</span>
    <span class="lead__bold">Ipsum Dolor</span>
  </div>
  <p class="body-copy" style="left:10%; top:56%; width:36%;">Lorem ipsum dolor sit amet, consectetur adipiscing elit, sed do eiusmod tempor incididunt ut labore et dolore magna aliqua. Ut enim ad minim veniam, quis nostrud exercitation.</p>
  <div class="photo" role="img" aria-label="Two colleagues working together at a machine in a workshop" style="left:51%; top:22%; width:44%; height:56%; background:linear-gradient(135deg,#c9ced3,#7f8790 60%,#4a5058);"></div>
  <svg class="accent-triangle" style="left:51%; top:69%;" viewBox="0 0 10 10" preserveAspectRatio="none" aria-hidden="true"><polygon points="0,0 10,10 0,10" fill="#2e7a3c"/></svg>
  <div class="slide__footer"><span class="slide__footer-title">vaultline Presentation Title 2023</span></div>
  <div class="page-tab">01</div>
</section>

<!-- Slide 02 -->
<section class="slide slide--small" style="left:66px; top:315px;">
  <svg class="facets" viewBox="0 0 728 515" preserveAspectRatio="none" aria-hidden="true">
    <rect width="728" height="515" fill="#f7f7f8"/>
    <polygon points="0,0 250,0 0,170" fill="#ffffff"/>
    <polygon points="728,200 728,515 280,515" fill="#ffffff"/>
  </svg>
  <h2 class="slide__header" style="top:10%;"><em>Header</em> Goes Here</h2>
  <div class="brand-name">Vaultline</div>
  <div class="photo" role="img" aria-label="Presenter speaking to a team in a bright brick-walled office" style="left:6%; top:24%; width:89%; height:36%; background:linear-gradient(90deg,#8a6d52,#b7977a 40%,#c9cdd2 75%,#8d939a);"></div>
  <svg class="accent-triangle" style="left:6%; top:54%;" viewBox="0 0 10 10" preserveAspectRatio="none" aria-hidden="true"><polygon points="0,0 10,10 0,10" fill="#2e7a3c"/></svg>

  <div class="feature" style="left:8%;">
    <svg class="feature__icon" viewBox="0 0 20 20" aria-hidden="true"><circle cx="10" cy="10" r="8" fill="none" stroke="#2e7a3c" stroke-width="1.6"/><polyline points="6,10 9,13 14,7" fill="none" stroke="#2e7a3c" stroke-width="1.6"/></svg>
    <div class="feature__title">Lorem ipsum</div>
    <p class="feature__text">Lorem ipsum dolor sit amet, consectetur adipiscing elit, sed do eiusmod tempor incididunt.</p>
  </div>
  <div class="feature" style="left:38%;">
    <svg class="feature__icon" viewBox="0 0 20 20" aria-hidden="true"><rect x="3" y="4" width="14" height="12" rx="2" fill="none" stroke="#2e7a3c" stroke-width="1.6"/><line x1="6" y1="9" x2="14" y2="9" stroke="#2e7a3c" stroke-width="1.6"/><line x1="6" y1="12" x2="11" y2="12" stroke="#2e7a3c" stroke-width="1.6"/></svg>
    <div class="feature__title">Lorem ipsum</div>
    <p class="feature__text">Lorem ipsum dolor sit amet, consectetur adipiscing elit, sed do eiusmod tempor incididunt.</p>
  </div>
  <div class="feature" style="left:68%;">
    <svg class="feature__icon" viewBox="0 0 20 20" aria-hidden="true"><line x1="2" y1="18" x2="18" y2="18" stroke="#2e7a3c" stroke-width="1.6"/><rect x="4" y="11" width="3" height="6" fill="none" stroke="#2e7a3c" stroke-width="1.4"/><rect x="9" y="7" width="3" height="10" fill="none" stroke="#2e7a3c" stroke-width="1.4"/><rect x="14" y="3" width="3" height="14" fill="none" stroke="#2e7a3c" stroke-width="1.4"/></svg>
    <div class="feature__title">Lorem ipsum</div>
    <p class="feature__text">Lorem ipsum dolor sit amet, consectetur adipiscing elit, sed do eiusmod tempor incididunt.</p>
  </div>

  <div class="slide__footer"><span class="slide__footer-title">vaultline Presentation Title 2023</span></div>
  <div class="page-tab">02</div>
</section>

<!-- Slide 03 -->
<section class="slide slide--small" style="left:456px; top:315px;">
  <svg class="facets" viewBox="0 0 728 515" preserveAspectRatio="none" aria-hidden="true">
    <rect width="728" height="515" fill="#f7f7f8"/>
    <polygon points="0,0 250,0 0,170" fill="#ffffff"/>
    <polygon points="400,0 728,0 728,80 460,280 200,280" fill="#eeeef0"/>
    <polygon points="728,200 728,515 300,515" fill="#ffffff"/>
  </svg>
  <h2 class="slide__header"><em>Header</em> Goes Here</h2>
  <div class="brand-name">Vaultline</div>
  <div class="photo" role="img" aria-label="Hand lifting the receiver of a desk telephone beside a plant" style="left:6%; top:27%; width:40%; height:56%; background:linear-gradient(135deg,#d6d9dc,#8c8f92 55%,#3e4044);"></div>
  <svg class="accent-triangle" style="left:39%; top:66%;" viewBox="0 0 10 10" preserveAspectRatio="none" aria-hidden="true"><polygon points="10,0 10,10 0,10" fill="#2e7a3c"/></svg>
  <div class="lead" style="left:52%; top:27%;">
    <span class="lead__light">Lorem</span>
    <span class="lead__bold">Ipsum Dolor</span>
  </div>
  <p class="body-copy" style="left:52%; top:49%; width:40%;">Lorem ipsum dolor sit amet, consectetur adipiscing elit, sed do eiusmod tempor incididunt ut labore et dolore magna aliqua. Ut enim ad minim veniam, quis nostrud exercitation.</p>
  <div class="slide__footer"><span class="slide__footer-title">vaultline Presentation Title 2023</span></div>
  <div class="page-tab">03</div>
</section>

<!-- Master content slide -->
<section class="slide slide--large">
  <svg class="facets" viewBox="0 0 728 515" preserveAspectRatio="none" aria-hidden="true">
    <defs>
      <linearGradient id="shadeBand" x1="0" y1="0" x2="1" y2="1">
        <stop offset="0" stop-color="#e2e3e6"/>
        <stop offset="1" stop-color="#f7f7f8"/>
      </linearGradient>
    </defs>
    <rect width="728" height="515" fill="#f6f6f7"/>
    <polygon points="0,0 190,0 0,130" fill="#ffffff"/>
    <polygon points="265,0 728,0 728,110 420,330 0,330 0,230" fill="url(#shadeBand)" opacity=".55"/>
    <polygon points="0,330 140,190 0,290" fill="#ffffff" opacity=".8"/>
    <polygon points="520,0 728,0 728,40 640,90" fill="#e6e7ea"/>
    <polygon points="728,190 728,515 330,515" fill="#ffffff"/>
    <polygon points="728,110 728,250 480,420 420,330" fill="#ffffff" opacity=".7"/>
    <polygon points="0,430 230,300 260,330 0,470" fill="#ffffff" opacity=".7"/>
  </svg>
  <h2 class="slide__header"><em>Header</em> Goes Here</h2>
  <div class="brand-name">Vaultline</div>
  <div class="slide__footer"><span class="slide__footer-title">vaultline Presentation Title 2023</span></div>
  <div class="page-tab">03</div>
</section>

</body>
</html>
```